Letterhead and Business Card for our company

We need a letterhead to our company with Business Cards.. This will be printed. The letter head is the official use for the company.

Note: Put in consideration that 2 languages will be used, you will design the English and we will add the Arabic.

Company name: Brisk Harbor
City: Jeddah
District: Alrehab
Center: Palmgate Plaza
Country: Saudi Arabia
POBox: 3872 Jeddah 23619

Industry/Entity Type

Startup

Font styles to use
Sans Serif

Requirements
Must have
• Capital: 100,000
• CR: 4817293058

```html
<!DOCTYPE html>
<html lang="en">
<head>
<meta charset="utf-8">
<title>Brisk Harbor — Letterhead and Business Cards</title>
<link href="https://fonts.googleapis.com/css2?family=Open+Sans:wght@400;600;700&display=swap" rel="stylesheet">
<style>
  :root{
    --bg:#ececec;
    --paper:#ffffff;
    --ink:#2b2b2b;
    --muted:#6d6d6d;
    --faint:#e6e6e6;
    --black:#1a1a1a;
    --blue:#2aa3d8;
    --green:#8cc63f;
    --pink:#e6197b;
    --brand:#3a3a3a;
  }
  *{box-sizing:border-box;margin:0;padding:0}
  html,body{width:1200px;height:765px;overflow:hidden}
  body{background:var(--bg);font-family:"Open Sans",Arial,sans-serif;color:var(--ink);position:relative}

  .paper{position:absolute;background:var(--paper);box-shadow:0 2px 10px rgba(0,0,0,.12);overflow:hidden}

  /* brand lockup */
  .brand{display:flex;align-items:center;gap:8px}
  .brand-dot{width:22px;height:22px;border-radius:50%;background:var(--blue)}
  .brand-name{font-weight:700;color:var(--brand);letter-spacing:.04em;text-transform:uppercase;font-size:15px;line-height:1}

  /* colour strip */
  .strip{position:absolute;left:0;right:0;bottom:0;height:7px;display:flex}
  .strip .seg-black{flex:1;background:var(--black)}
  .strip .seg-blue{width:14%;background:var(--blue)}
  .strip .seg-green{width:9%;background:var(--green)}
  .strip .seg-pink{width:6%;background:var(--pink)}

  /* letterhead */
  .letterhead{left:80px;top:30px;width:496px;height:702px;padding:44px 44px 0 44px}
  .letter{margin-top:34px;font-size:8.4px;line-height:1.55;color:var(--muted)}
  .letter p{margin-bottom:9px}
  .letter .meta{margin-bottom:12px}
  .signature{width:92px;height:26px;margin:4px 0 2px;background:linear-gradient(90deg,#e4e4e4,#f2f2f2);border-radius:3px}
  .letter .role{color:var(--ink);font-weight:600}
  .watermark{position:absolute;right:42px;top:330px;font-size:44px;font-weight:700;color:var(--faint);letter-spacing:.04em;text-transform:uppercase}
  .lh-footer{position:absolute;left:44px;right:44px;bottom:18px;font-size:7px;color:var(--muted);text-align:right;line-height:1.6}

  /* cards */
  .card{width:350px;height:200px}
  .card-front{left:700px;top:470px;display:flex;align-items:center;justify-content:center}
  .card-front .brand-name{font-size:24px}
  .card-front .brand-dot{width:36px;height:36px}
  .card-back{left:760px;top:210px;padding:26px 28px}
  .card-back .brand{position:absolute;right:24px;top:24px}
  .card-back .brand-name{font-size:12px}
  .card-back .brand-dot{width:18px;height:18px}
  .person{margin-top:58px;font-size:10px;font-weight:700;letter-spacing:.04em;color:var(--ink)}
  .person-title{font-size:7.5px;color:var(--muted);margin-bottom:8px}
  .contact{list-style:none;font-size:7.5px;color:var(--muted);line-height:1.9}
  .contact li{display:flex;align-items:center;gap:6px}
  .contact svg{width:8px;height:8px;fill:var(--blue)}
  .card-address{position:absolute;left:28px;bottom:16px;font-size:6.5px;color:var(--muted)}
  .card .strip{height:6px}
</style>
</head>
<body>

<section class="paper letterhead" aria-label="Letterhead">
  <div class="brand"><span class="brand-dot"></span><span class="brand-name">Brisk Harbor</span></div>

  <div class="letter">
    <div class="meta">
      <p>November 1, 2015<br>Mr. Owen Castell<br>88 Quill Road<br>Leicester, LE 4 7QT</p>
    </div>
    <p>Dear Mr. Castell,</p>
    <p>The first paragraph of a typical business letter is used to state the main point of the letter. Begin with a friendly opening, then quickly transition into the purpose of your letter. Use a couple of sentences to explain the purpose, but do not go into detail until the next paragraph.</p>
    <p>Beginning with the second paragraph, state the supporting details to justify your purpose. These may take the form of background information, statistics or first-hand accounts. A few short paragraphs within the body of the letter should be enough to support your reasoning.</p>
    <p>Finally, in the closing paragraph, briefly restate your purpose and why it is important. If the purpose of your letter is related to your employment, consider ending your letter with your contact information and title if it is not included on letterhead.</p>
    <p>Sincerely,</p>
    <div class="signature" role="img" aria-label="Handwritten signature"></div>
    <p class="role">Nadim Farouk<br>President</p>
  </div>

  <div class="watermark" aria-hidden="true">Brisk Harbor</div>

  <div class="lh-footer">
    Palmgate Plaza, Alrehab · P.O.Box: 3872 Jeddah 23619 · Saudi Arabia · info@briskharbor.com | www.briskharbor.com<br>
    Capital: 100,000 | CR: 4817293058
  </div>
  <div class="strip"><span class="seg-black"></span><span class="seg-blue"></span><span class="seg-green"></span><span class="seg-pink"></span></div>
</section>

<section class="paper card card-back" aria-label="Business card, back">
  <div class="brand"><span class="brand-dot"></span><span class="brand-name">Brisk Harbor</span></div>
  <p class="person">RAMI HADDAD</p>
  <p class="person-title">Chief Executive Officer</p>
  <ul class="contact">
    <li><svg viewBox="0 0 10 10"><path d="M2 0h2l1 3-1.5 1a6 6 0 0 0 2.5 2.5L7 5l3 1v2a2 2 0 0 1-2 2A8 8 0 0 1 0 2a2 2 0 0 1 2-2z"/></svg>+966 12 555 0147</li>
    <li><svg viewBox="0 0 10 10"><path d="M0 2h10v6H0z M0 2l5 3 5-3" /></svg>rami@briskharbor.com</li>
    <li><svg viewBox="0 0 10 10"><circle cx="5" cy="5" r="5"/></svg>www.briskharbor.com</li>
  </ul>
  <p class="card-address">P.O.Box: 3872 Jeddah 23619 · Saudi Arabia</p>
  <div class="strip"><span class="seg-black"></span><span class="seg-blue"></span><span class="seg-green"></span><span class="seg-pink"></span></div>
</section>

<section class="paper card card-front" aria-label="Business card, front">
  <div class="brand"><span class="brand-dot"></span><span class="brand-name">Brisk Harbor</span></div>
</section>

</body>
</html>
```